plumrivet-loans.com

We are a small dollar lending company that will revolutionize the industry. We will do this by being completely transparent, fee free, etc and an interest rate that normal people can afford to pay. Over 10X less than our competition. We only allow our members to pay bills " bills paid fast", within 72 hours. Payday loans typically charge from 390%-600% with a terrible payback structure. We charge 36%, period, with a payback structure over 12 months. Our site will be very simple and easy to use but elegant at the same time. We do not want the site to be too busy, less is more and easier. We will have; Home, The Story, Why Plumrivet.com, Are you eligible? Members, Clients. To become a member you have to be referred by a current client of Plumrivet.com. A lot of the busy stuff will be saved for the Members and Clients sections. The feel must be elegant, easy to use and very simple to understand. I am looking for the green, white and black combinations of colors, very similar to my logo that was designed by ArtHively.

```html
<!DOCTYPE html>
<html lang="en">
<head>
<meta charset="utf-8">
<title>Plumrivet — Bills Paid Fast</title>
<link href="https://fonts.googleapis.com/css2?family=Roboto:wght@300;400;700&display=swap" rel="stylesheet">
<style>
:root{
  --green:#7dc242;
  --green-dark:#5f9e2a;
  --green-light:#94d158;
  --ink:#111;
  --text:#444;
  --muted:#777;
  --line:#e3e3e3;
  --bg:#fff;
}
*{box-sizing:border-box;margin:0;padding:0}
html,body{width:1200px;height:1094px;overflow:hidden;background:var(--bg)}
body{font-family:"Roboto",Arial,sans-serif;color:var(--text);position:relative}
.page{position:absolute;left:161px;top:0;width:878px;height:1094px}
a{color:inherit;text-decoration:none}

/* header */
.brand{position:absolute;left:0;top:24px;display:flex;align-items:center;gap:10px}
.brand-dot{width:44px;height:44px;border-radius:50%;background:var(--green)}
.brand-name{font-size:31px;font-weight:400;color:var(--ink);letter-spacing:.5px}
.social{position:absolute;display:flex;gap:9px}
.social span{width:21px;height:21px;border-radius:3px;background:#b9b9b9}
.social--top{right:0;top:22px}
.phone{position:absolute;right:131px;top:61px;display:flex;align-items:center;gap:6px;font-size:15px;color:var(--ink)}
.btn-dark{display:inline-block;background:linear-gradient(#3a3a3a,#000);color:#fff;font-weight:700;font-size:12px;border-radius:3px;text-align:center}
.login{position:absolute;right:0;top:57px;width:112px;height:26px;line-height:26px}

/* nav */
.nav{position:absolute;left:0;top:114px;width:878px;height:33px;border-radius:3px;background:linear-gradient(var(--green-light),var(--green) 55%,var(--green-dark));display:flex;overflow:hidden}
.nav a{height:33px;line-height:33px;text-align:center;color:#fff;font-size:12px;border-right:1px solid rgba(0,0,0,.12)}
.nav a.active{background:linear-gradient(#444,#000 60%,#111)}

/* hero */
.hero{position:absolute;left:0;top:172px;width:878px;height:309px;border:1px solid #d8d8d8;border-radius:3px;overflow:hidden}
.hero-photo{position:absolute;left:0;top:0;width:470px;height:100%;background:linear-gradient(90deg,#e9e6e2,#f4f2ef 70%,#fff)}
.hero-copy{position:absolute;left:515px;top:38px}
.hero-title{font-size:38px;font-weight:300;color:var(--green)}
.hero-list{list-style:none;margin-top:18px}
.hero-list li{display:flex;align-items:center;gap:12px;font-size:14px;color:#333;height:34px}
.btn-green{display:inline-block;margin-top:18px;width:120px;height:35px;line-height:35px;text-align:center;color:#fff;font-size:18px;background:linear-gradient(var(--green-light),var(--green-dark));border-radius:3px}

/* features */
.features{position:absolute;left:0;top:503px;width:878px;height:84px;display:flex}
.feature{display:flex;align-items:center;gap:16px;height:84px}
.feature + .feature{border-left:1px solid var(--line)}
.feature-icon{width:60px;height:60px;border-radius:50%;background:var(--green);display:flex;align-items:center;justify-content:center;flex:none}
.feature h3{font-size:23px;font-weight:400;color:var(--ink)}
.feature p{font-size:14px;color:var(--muted);font-weight:300;margin-top:4px}
.rule{position:absolute;left:0;width:878px;height:1px;background:var(--line)}

/* content */
.section-title{font-size:22px;font-weight:300;color:var(--green);text-decoration:underline;text-underline-offset:3px}
.story{position:absolute;left:0;top:667px;width:500px}
.story p{margin-top:16px;font-size:12.3px;line-height:16px;color:#555}
.story .btn-dark{margin-top:31px;width:83px;height:26px;line-height:26px}
.vline{position:absolute;left:562px;top:672px;width:1px;height:241px;background:var(--line)}
.why{position:absolute;left:631px;top:667px}
.why ul{list-style:none;margin-top:12px}
.why li{display:flex;align-items:center;gap:11px;font-size:12.3px;color:var(--muted);font-weight:300;height:21px}

/* footer */
.footer-links{position:absolute;left:0;top:998px;font-size:11.5px;color:#444}
.footer-links a.current{color:var(--green);text-decoration:underline}
.footer-links i{font-style:normal;margin:0 10px}
.social--foot{left:3px;top:1036px}
.footer-brand{position:absolute;right:0;top:1000px;display:flex;align-items:center;gap:8px}
.footer-brand .brand-dot{width:34px;height:34px}
.footer-brand .brand-name{font-size:22px}
.footer-brand small{font-size:14px;color:#888;margin-left:4px}
</style>
</head>
<body>
<div class="page">
  <header>
    <a class="brand" href="#"><span class="brand-dot"></span><span class="brand-name">Plumrivet</span></a>
    <div class="social social--top" aria-label="Social links"><span></span><span></span><span></span><span></span><span></span></div>
    <div class="phone">
      <svg width="13" height="13" viewBox="0 0 24 24"><path fill="#777" d="M6.6 10.8a15 15 0 0 0 6.6 6.6l2.2-2.2c.3-.3.7-.4 1-.2 1.1.4 2.3.6 3.6.6.6 0 1 .4 1 1V20c0 .6-.4 1-1 1A17 17 0 0 1 3 4c0-.6.4-1 1-1h3.5c.6 0 1 .4 1 1 0 1.3.2 2.5.6 3.6.1.3 0 .7-.2 1z"/></svg>
      555.014.227
    </div>
    <a class="btn-dark login" href="#">Members Login</a>
  </header>

  <nav class="nav">
    <a class="active" href="#" style="width:95px">Home</a>
    <a href="#" style="width:107px">The Story</a>
    <a href="#" style="width:140px">Why Plumrivet.com</a>
    <a href="#" style="width:145px">Are You Eligible?</a>
    <a href="#" style="width:105px">Members</a>
    <a href="#" style="width:97px">Clients</a>
  </nav>

  <section class="hero">
    <div class="hero-photo" role="img" aria-label="Family of three smiling around a laptop on a white sofa"></div>
    <div class="hero-copy">
      <h1 class="hero-title">Bills Paid Fast</h1>
      <ul class="hero-list">
        <li><svg width="16" height="14" viewBox="0 0 16 14"><path d="M1 7.5l4.5 4.5L15 1.5" fill="none" stroke="#111" stroke-width="3"/></svg>WE CHARGE 36% ...</li>
        <li><svg width="16" height="14" viewBox="0 0 16 14"><path d="M1 7.5l4.5 4.5L15 1.5" fill="none" stroke="#111" stroke-width="3"/></svg>MEMBERS PAY BILLS WITHIN 72 HOURS</li>
        <li><svg width="16" height="14" viewBox="0 0 16 14"><path d="M1 7.5l4.5 4.5L15 1.5" fill="none" stroke="#111" stroke-width="3"/></svg>12 MONTHS PAYBACK STRUCTURE</li>
      </ul>
      <a class="btn-green" href="#">APPLY NOW</a>
    </div>
  </section>

  <section class="features">
    <div class="feature" style="width:281px">
      <span class="feature-icon"><svg width="34" height="30" viewBox="0 0 34 30"><rect x="2" y="3" width="30" height="19" rx="1" fill="none" stroke="#fff" stroke-width="3"/><path d="M12 28h10M17 22v6" stroke="#fff" stroke-width="3"/><path d="M10 17l12-11" stroke="#fff" stroke-width="2.5"/></svg></span>
      <div><h3>Apply Online</h3><p>100% Online Application</p></div>
    </div>
    <div class="feature" style="width:309px;padding-left:38px">
      <span class="feature-icon"><svg width="32" height="26" viewBox="0 0 32 26"><path d="M3 13l9 9L29 4" fill="none" stroke="#fff" stroke-width="5"/></svg></span>
      <div><h3>Get Approved</h3><p>Total Market Coverage</p></div>
    </div>
    <div class="feature" style="width:288px;padding-left:41px">
      <span class="feature-icon"><svg width="30" height="34" viewBox="0 0 30 34"><path d="M10 2h10l-3 6h-4z" fill="#fff"/><ellipse cx="15" cy="22" rx="12" ry="11" fill="#fff"/><text x="15" y="27" text-anchor="middle" font-family="Roboto,Arial,sans-serif" font-weight="700" font-size="14" fill="#7dc242">$</text></svg></span>
      <div><h3>Get Your Cash</h3><p>No Hidden Fees or Charges</p></div>
    </div>
  </section>
  <div class="rule" style="top:615px"></div>

  <section class="story">
    <h2 class="section-title">Our Story</h2>
    <p>Small dollar loans are either too hard to get, take too long to process or just impossible to pay back. &nbsp;There are between 15mm-18mm people each year that require the use of small dollar loans, so you are not alone. Let's face it we are all short on cash at some point. At plumrivet-loans.com we have created a product that is very accessible, has a quick turnaround and best of all the payback terms are very reasonable ...</p>
    <a class="btn-dark" href="#">Read More</a>
  </section>
  <div class="vline"></div>
  <section class="why">
    <h2 class="section-title">Why Choose Us ?</h2>
    <ul>
      <li><svg width="12" height="10" viewBox="0 0 12 10"><path d="M1 5l3.5 3.5L11 1" fill="none" stroke="#999" stroke-width="2.2"/></svg>Poor Credit is OK!</li>
      <li><svg width="12" height="10" viewBox="0 0 12 10"><path d="M1 5l3.5 3.5L11 1" fill="none" stroke="#999" stroke-width="2.2"/></svg>No hidden fees or charges</li>
      <li><svg width="12" height="10" viewBox="0 0 12 10"><path d="M1 5l3.5 3.5L11 1" fill="none" stroke="#999" stroke-width="2.2"/></svg>No faxing of documents</li>
      <li><svg width="12" height="10" viewBox="0 0 12 10"><path d="M1 5l3.5 3.5L11 1" fill="none" stroke="#999" stroke-width="2.2"/></svg>Borrow between $300-$7000</li>
      <li><svg width="12" height="10" viewBox="0 0 12 10"><path d="M1 5l3.5 3.5L11 1" fill="none" stroke="#999" stroke-width="2.2"/></svg>Quick and simple 60 second application</li>
      <li><svg width="12" height="10" viewBox="0 0 12 10"><path d="M1 5l3.5 3.5L11 1" fill="none" stroke="#999" stroke-width="2.2"/></svg>No Security needed</li>
      <li><svg width="12" height="10" viewBox="0 0 12 10"><path d="M1 5l3.5 3.5L11 1" fill="none" stroke="#999" stroke-width="2.2"/></svg>7 days a week, 365 days a year</li>
      <li><svg width="12" height="10" viewBox="0 0 12 10"><path d="M1 5l3.5 3.5L11 1" fill="none" stroke="#999" stroke-width="2.2"/></svg>Get a decision in seconds</li>
      <li><svg width="12" height="10" viewBox="0 0 12 10"><path d="M1 5l3.5 3.5L11 1" fill="none" stroke="#999" stroke-width="2.2"/></svg>100% online application</li>
      <li><svg width="12" height="10" viewBox="0 0 12 10"><path d="M1 5l3.5 3.5L11 1" fill="none" stroke="#999" stroke-width="2.2"/></svg>Safe &amp; secure</li>
    </ul>
  </section>

  <footer>
    <div class="rule" style="top:970px;background:linear-gradient(90deg,#fff,#ddd 20%,#ddd 80%,#fff)"></div>
    <div class="footer-links">
      <a class="current" href="#">Home</a><i>-</i><a href="#">The Story</a><i>-</i><a href="#">Why Plumrivet.com</a><i>-</i><a href="#">Are You Eligible?</a><i>-</i><a href="#">Members</a><i>-</i><a href="#">Clients</a><i>-</i><a href="#">Terms of use</a>
    </div>
    <div class="social social--foot" aria-label="Social links"><span></span><span></span><span></span><span></span><span></span></div>
    <div class="footer-brand"><span class="brand-dot"></span><span class="brand-name">Plumrivet</span><small>© 2014.</small></div>
  </footer>
</div>
</body>
</html>
```